Titelseite und Rückseite für Schraubenkatalog gesucht
Zielgruppe
KOR Fügesysteme GmbH verkauft Schrauben, Werkzeuge, Industriebedarf,Betriebsausstattung, Arbeitsschutz, an große und kleine Firmen.
Für einen Schraubenkatalog soll die Titel Seite und die Rückseite gestaltet werden, Größe A4
Kontaktdaten auf der Webseite www.kor-Fuegesysteme.de
Der Wunsch des Kunden ist es soll sehr hochwertig, edel aussehen.
Das Logo und natürlich die Kontaktdaten sollen mit drauf sein.
Aufgabenstellung
Vielleicht eine Schraube oder Mutter oder........
Der Spruch: Wir halten zusammen, was zusammen gehört.' soll mit eingebaut werden
Wir werden gegen Abend alle Vorschläge bewerten nach Absprache mit dem Kunden.
Vielen Dank für Ihre Vorschläge schon mal.

```html
<!DOCTYPE html>
<html lang="de">
<head>
<meta charset="utf-8">
<title>KOR Fügesysteme GmbH – Katalog Rückseite</title>
<link rel="stylesheet" href="https://fonts.googleapis.com/css2?family=Jost:wght@400;600&family=Arimo&display=swap">
<style>
  :root {
    --sky-top: #3b7688;
    --sky-mid: #6ea3b0;
    --haze: #8fb3ad;
    --water: #3f88a8;
    --skin: #9a6a4a;
    --shadow: #2f3338;
    --grass: #6b6a3a;
    --ground: #3e3a22;
    --brand-red: #e0161c;
    --steel: #c9cdd1;
    --text-light: #ffffff;
  }
  html, body {
    margin: 0;
    padding: 0;
    overflow: hidden;
  }
  .page {
    position: relative;
    width: 855px;
    height: 1200px;
    overflow: hidden;
    font-family: "Jost", sans-serif;
    background: var(--sky-top);
  }
  .sky {
    position: absolute;
    inset: 0 0 auto 0;
    height: 560px;
    background: linear-gradient(to bottom, var(--sky-top) 0%, #4f8799 40%, var(--sky-mid) 100%);
  }
  .hero-photo {
    position: absolute;
    left: 0;
    top: 500px;
    width: 855px;
    height: 700px;
    background:
      radial-gradient(ellipse 55% 40% at 28% 55%, rgba(154,106,74,0.75), rgba(154,106,74,0) 70%),
      radial-gradient(ellipse 30% 45% at 85% 45%, rgba(120,90,70,0.6), rgba(120,90,70,0) 70%),
      linear-gradient(to bottom,
        rgba(110,163,176,0) 0%,
        var(--haze) 18%,
        #5f7f6a 32%,
        var(--water) 45%,
        #3d6f86 62%,
        var(--shadow) 74%,
        var(--grass) 86%,
        var(--ground) 100%);
  }
  .brand {
    position: absolute;
    top: 226px;
    left: 0;
    width: 100%;
    display: flex;
    justify-content: center;
    align-items: center;
    gap: 14px;
  }
  .brand-mark {
    width: 34px;
    height: 34px;
    background: var(--brand-red);
  }
  .brand-name {
    margin: 0;
    font-weight: 600;
    font-size: 40px;
    line-height: 48px;
    letter-spacing: 0.5px;
    color: var(--brand-red);
    text-transform: uppercase;
  }
  .brand-rule {
    position: absolute;
    top: 286px;
    left: 162px;
    width: 554px;
    height: 2px;
    background: var(--steel);
  }
  .contact {
    position: absolute;
    top: 330px;
    left: 0;
    width: 100%;
    text-align: center;
    color: var(--text-light);
    font-size: 17px;
    line-height: 24px;
    font-style: normal;
  }
  .contact p { margin: 0; }
  .contact .phone {
    font-family: "Arimo", sans-serif;
    font-size: 16px;
  }
  .claim {
    position: absolute;
    left: 0;
    bottom: 48px;
    width: 100%;
    display: flex;
    flex-direction: column;
    align-items: center;
    gap: 12px;
  }
  .claim-nut {
    width: 36px;
    height: 36px;
  }
  .claim-text {
    margin: 0;
    font-size: 26px;
    font-weight: 600;
    color: var(--text-light);
    letter-spacing: 0.5px;
  }
</style>
</head>
<body>
  <main class="page">
    <div class="sky"></div>
    <div class="hero-photo" role="img" aria-label="Foto: zwei Männer sitzen am Flussufer im Sommer und reichen sich die Hand zum festen Griff, Flaschen im Gras, Stadtsilhouette im Hintergrund"></div>

    <header class="brand">
      <span class="brand-mark" aria-hidden="true"></span>
      <h1 class="brand-name">KOR Fügesysteme GmbH</h1>
    </header>
    <div class="brand-rule" aria-hidden="true"></div>

    <address class="contact">
      <p>KOR Fügesysteme GmbH Chemnitz</p>
      <p>Lindenhofstr. 14, 09116 Chemnitz</p>
      <p class="phone">+49 (0) 371 5550192</p>
      <p>info@kor-fuegesysteme.de</p>
      <p>www.kor-Fuegesysteme.de</p>
    </address>

    <section class="claim">
      <svg class="claim-nut" viewBox="0 0 36 36" aria-hidden="true">
        <polygon points="18,2 32,10 32,26 18,34 4,26 4,10" fill="none" stroke="var(--steel)" stroke-width="3"/>
        <circle cx="18" cy="18" r="6" fill="none" stroke="var(--steel)" stroke-width="3"/>
      </svg>
      <p class="claim-text">Wir halten zusammen, was zusammen gehört.</p>
    </section>
  </main>
</body>
</html>
```